Digital agency needs a new web design

We’re looking to redesign our website – so that it is 3 things: smart, stylish and simplistic.
Plenix are a digital performance agency, offering services in PPC. SEO. Analytics, Display, Content and Paid Social, and we work with fantastic clients.
Our current website isn't reflective of how forward-thinking we are as an agency, and doesn't convey our two USPs well - our technology and our network of digital marketing experts. So we're looking to build a clear and concise site that attracts both inbound leads and digital marketing professionals to join our team or our Plenixer network.
You can take a look at our current website here - http://plenix-example.com/. The copy will change and we happy for the colours to change.

Target Market(s)

The primary target audience is marketing directors, digital directors, marketing managers and online acquisition managers. The secondary audience are people in the industry looking for work either as permanent employees or as part of the Plenix freelance network.

Industry/Entity Type

Marketing

Number of Pages Required

5+ page

Font styles to use
Sans Serif

Requirements
Must have
• - A stylish/ grown-up feel
• - Be of a design/ templates that can be editable
• - A really clear concise/ homepage
• The homepage must include:
• 1. A reference to our services
• 2. A reference to our network of digital marketing experts
• 3. A reference to our technology
• 4. A section for case studies
• 5. A section for our blog
• 6. A newsletter signup
• Th copy will be changed so please don't feel like you need to keep that.
Should not have
• - Cartoon style images as on the site on the moment
• - You should not have to scroll very far to find out what we do

```html
<!DOCTYPE html>
<html lang="en">
<head>
<meta charset="utf-8">
<title>Plenix — Digital Performance Agency</title>
<link rel="stylesheet" href="https://fonts.googleapis.com/css2?family=Open+Sans:wght@400;600;700&family=Raleway:wght@600;700&display=swap">
<style>
:root{
  --ink:#222426;
  --text:#555a60;
  --muted:#8a8f95;
  --light:#f6f6f6;
  --white:#ffffff;
  --dark:#1d1f22;
  --dark-2:#2a2c30;
  --line:#9aa0a6;
  --accent:#2196e8;
  --overlay:rgba(20,22,26,.72);
}
*{box-sizing:border-box;margin:0;padding:0}
html,body{width:1200px;height:3509px;overflow:hidden;background:var(--white)}
body{font-family:"Open Sans",Arial,sans-serif;color:var(--text)}
.page{position:relative;width:1200px;height:3509px;overflow:hidden}
.abs{position:absolute}
.heading{font-family:"Raleway",Arial,sans-serif;font-weight:700;color:var(--ink)}
.btn{position:absolute;display:flex;align-items:center;justify-content:center;border:2px solid var(--ink);font-size:11px;font-weight:600;letter-spacing:.5px;color:var(--ink);text-transform:uppercase}
.btn--light{border-color:var(--white);color:var(--white)}

/* Hero */
.hero{position:absolute;left:0;top:0;width:1200px;height:561px;
  background:linear-gradient(180deg,#2e3643 0%,#3d4656 35%,#6a5a58 55%,#4a4a50 70%,#2b2f36 100%)}
.hero__shade{position:absolute;inset:0;background:rgba(15,18,24,.25)}
.brand{position:absolute;left:133px;top:46px;display:flex;align-items:center;gap:10px;color:var(--white);font-size:28px;font-weight:600}
.brand__dot{width:22px;height:22px;border:2px solid var(--white);border-radius:50%}
.nav{position:absolute;top:58px;left:508px;font-size:11px;color:var(--white);letter-spacing:.3px}
.nav span{position:absolute;white-space:nowrap}
.hero__play{position:absolute;left:554px;top:215px}
.hero__title{position:absolute;left:0;top:333px;width:1200px;text-align:center;color:var(--white);font-weight:700;font-size:23px;line-height:36px}
.dots{position:absolute;top:502px;left:570px;display:flex;gap:6px}
.dots i{width:11px;height:11px;border-radius:50%;background:var(--white);display:block}
.dots i.on{background:var(--accent)}

/* Services */
.services{position:absolute;left:0;top:561px;width:1200px;height:405px;background:var(--light)}
.service{position:absolute;width:180px;text-align:center}
.service__label{font-size:11px;font-weight:700;color:var(--ink);letter-spacing:.5px}
.service__text{font-size:10px;line-height:15px;color:var(--text)}
.service__icon{position:absolute;width:66px;height:66px;border:2px solid var(--line);border-radius:50%;background:var(--white);display:flex;align-items:center;justify-content:center}
.vline{position:absolute;width:2px;background:var(--line)}

/* Clients */
.clients{position:absolute;left:0;top:966px;width:1200px;height:285px;
  background:linear-gradient(90deg,#151618 0%,#2c2d30 40%,#3a3a3d 60%,#1a1b1d 100%)}
.clients__text{position:absolute;left:150px;top:1034px;width:900px;text-align:center;color:#e6e6e6;font-size:11px;line-height:19px}
.client{position:absolute;top:1136px;width:170px;margin-left:-85px;text-align:center;color:var(--white);font-family:"Open Sans",Arial,sans-serif;font-weight:700;font-size:20px;line-height:28px;white-space:nowrap}

/* Network */
.network{position:absolute;left:0;top:1251px;width:1200px;height:480px;background:var(--light)}
.globe{position:absolute;left:737px;top:1352px;width:290px;height:290px;border-radius:50%;border:2px solid #c8c8c8;padding:10px}
.globe__fill{width:100%;height:100%;border-radius:50%;background:radial-gradient(circle at 45% 45%,#ffffff 0%,#e4e4e4 60%,#bfbfbf 100%);border:2px solid #4a4a4a}

/* Technology */
.tech{position:absolute;left:0;top:1731px;width:1200px;height:332px;
  background:radial-gradient(circle at 70% 60%,#3a3d44 0%,#1c1e22 55%,#131417 100%)}
.tech__text{position:absolute;left:250px;top:1856px;width:700px;text-align:center;color:#e8e8e8;font-size:11px;line-height:19px}

/* Feature cards */
.card{position:absolute;top:2068px;height:393px;overflow:hidden}
.card__date{position:absolute;color:var(--white);font-weight:700;font-size:15px}
.card__text{position:absolute;color:var(--white);font-size:14px;line-height:22px}

/* Case studies */
.cases{position:absolute;left:0;top:2461px;width:1200px;height:627px;background:var(--light)}
.case__img{position:absolute;top:2636px;width:274px;height:190px}
.case__title{position:absolute;top:2845px;font-family:"Raleway",Arial,sans-serif;font-weight:700;font-size:20px;color:var(--ink)}
.case__text{position:absolute;top:2880px;width:274px;font-size:10.5px;line-height:16px;color:var(--text)}

/* Contact */
.contact{position:absolute;left:0;top:3088px;width:1200px;height:421px;
  background:linear-gradient(180deg,#2a2b2e 0%,#232427 100%)}
.field{position:absolute;border:1px solid #55585d;color:#dcdcdc;font-size:10px;padding:0 12px;display:flex;align-items:center}
.submit{position:absolute;left:578px;top:3383px;width:86px;height:34px;background:var(--accent);color:var(--white);font-size:11px;font-weight:700;display:flex;align-items:center;justify-content:center}
.info{position:absolute;top:3253px;width:170px;color:#e0e0e0;font-size:10.5px;line-height:16px}
.social{position:absolute;top:3366px;left:713px;display:flex;gap:17px}
.social i{display:block;width:16px;height:16px;border-radius:50%;background:#e0e0e0}
.footer-line{position:absolute;left:0;top:3450px;width:1200px;height:1px;background:#3c3e42}
.copyright{position:absolute;left:0;top:3470px;width:1200px;text-align:center;color:#bdbdbd;font-size:10px}
</style>
</head>
<body>
<div class="page">

  <!-- Hero -->
  <section class="hero" role="img" aria-label="City skyline at dusk with office towers"></section>
  <div class="hero__shade"></div>
  <div class="brand"><span class="brand__dot"></span>Plenix</div>
  <nav class="nav">
    <span style="left:0">SERVICES</span>
    <span style="left:96px">ABOUT PLENIX</span>
    <span style="left:222px">OUR WORK</span>
    <span style="left:332px">BLOG</span>
    <span style="left:412px">JOIN US</span>
    <span style="left:502px">CONTACT US</span>
  </nav>
  <svg class="hero__play" width="94" height="94" viewBox="0 0 94 94" aria-hidden="true">
    <circle cx="47" cy="47" r="44" fill="rgba(255,255,255,.15)" stroke="#fff" stroke-width="3"/>
    <path d="M38 30 L64 47 L38 64 Z" fill="#fff"/>
  </svg>
  <h1 class="hero__title">We are a digital performance agency, offering services in PPC,<br>SEO, Analytics, Display, Content and Paid Social.</h1>
  <div class="dots"><i></i><i></i><i class="on"></i><i></i></div>

  <!-- Services timeline -->
  <section class="services"></section>

  <div class="vline" style="left:231px;top:561px;height:154px"></div>
  <div class="vline" style="left:525px;top:561px;height:154px"></div>
  <div class="vline" style="left:818px;top:561px;height:154px"></div>
  <div class="vline" style="left:378px;top:824px;height:142px"></div>
  <div class="vline" style="left:670px;top:824px;height:142px"></div>
  <div class="vline" style="left:965px;top:824px;height:142px"></div>

  <!-- SEO -->
  <div class="service__icon" style="left:199px;top:715px">
    <svg width="30" height="30" viewBox="0 0 30 30" fill="none" stroke="#444" stroke-width="2"><circle cx="15" cy="15" r="10"/><circle cx="15" cy="15" r="4"/></svg>
  </div>
  <div class="service" style="left:142px;top:796px"><div class="service__label">SEO</div><p class="service__text">Sed ut perspiciatis unde omnis iste natus sit voluptatem accusantium doloremque.</p></div>

  <!-- Analytics -->
  <div class="service" style="left:289px;top:668px"><p class="service__text">Sed ut perspiciatis unde omnis iste natus sit voluptatem accusantium doloremque.</p><div class="service__label" style="margin-top:8px">ANALYTICS</div></div>
  <div class="service__icon" style="left:346px;top:758px">
    <svg width="30" height="30" viewBox="0 0 30 30" fill="none" stroke="#444" stroke-width="2"><path d="M4 4 V26 H26"/><path d="M7 21 L13 13 L18 18 L25 9"/></svg>
  </div>

  <!-- Display -->
  <div class="service__icon" style="left:493px;top:715px">
    <svg width="30" height="30" viewBox="0 0 30 30" fill="none" stroke="#444" stroke-width="2"><rect x="5" y="5" width="20" height="20"/><path d="M9 21 L21 9"/></svg>
  </div>
  <div class="service" style="left:436px;top:796px"><div class="service__label">DISPLAY</div><p class="service__text">Sed ut perspiciatis unde omnis iste natus sit voluptatem accusantium doloremque.</p></div>

  <!-- Content -->
  <div class="service" style="left:581px;top:668px"><p class="service__text">Sed ut perspiciatis unde omnis iste natus sit voluptatem accusantium doloremque.</p><div class="service__label" style="margin-top:8px">CONTENT</div></div>
  <div class="service__icon" style="left:638px;top:758px">
    <svg width="30" height="30" viewBox="0 0 30 30" fill="none" stroke="#444" stroke-width="2"><rect x="7" y="4" width="16" height="22"/><path d="M11 10 H19 M11 15 H19 M11 20 H17"/></svg>
  </div>

  <!-- Paid Social -->
  <div class="service__icon" style="left:786px;top:715px">
    <svg width="30" height="30" viewBox="0 0 30 30" fill="none" stroke="#444" stroke-width="2"><rect x="4" y="6" width="22" height="18"/><path d="M6 22 L12 14 L17 19 L20 16 L25 22"/></svg>
  </div>
  <div class="service" style="left:729px;top:796px"><div class="service__label">PAID SOCIAL</div><p class="service__text">Sed ut perspiciatis unde omnis iste natus sit voluptatem accusantium doloremque.</p></div>

  <!-- PPC -->
  <div class="service" style="left:876px;top:668px"><p class="service__text">Sed ut perspiciatis unde omnis iste natus sit voluptatem accusantium doloremque.</p><div class="service__label" style="margin-top:8px">PPC</div></div>
  <div class="service__icon" style="left:933px;top:758px">
    <svg width="30" height="30" viewBox="0 0 30 30" fill="none" stroke="#444" stroke-width="2"><circle cx="15" cy="15" r="11"/><circle cx="15" cy="15" r="6"/><circle cx="15" cy="15" r="1.5" fill="#444"/></svg>
  </div>

  <!-- Clients -->
  <section class="clients" role="img" aria-label="Dimmed office interior behind client names"></section>
  <p class="clients__text">Sed ut perspiciatis unde omnis iste natus error sit voluptatem accusantium doloremque laudantium, totam rem aperiam, eaque ipsa quae ab illo inventore veritatis et quasi architecto beatae vitae dicta sunt explicabo. Nemo enim ipsam voluptatem quia voluptas sit aspernatur aut odit aut fugit, sed quia consequuntur magni dolores eos qui ratione voluptatem sequi nesciunt.</p>
  <div class="client" style="left:255px;width:200px;margin-left:-100px">Harbourline Bank</div>
  <div class="client" style="left:432px">The Meridian</div>
  <div class="client" style="left:606px">HALDRAK</div>
  <div class="client" style="left:788px">STREAMORA</div>
  <div class="client" style="left:960px">R.J.Ashcombe</div>

  <!-- Our Network -->
  <section class="network"></section>
  <h2 class="heading abs" style="left:161px;top:1360px;font-size:33px">Our Network</h2>
  <p class="abs" style="left:161px;top:1424px;font-size:21px;font-weight:600;color:#3a3d42;line-height:29px">Technology should enhance<br><span style="color:var(--accent)">everything</span> that we do</p>
  <p class="abs" style="left:161px;top:1496px;width:380px;font-size:10.5px;line-height:17px">Sed ut perspiciatis unde omnis iste natus error sit voluptatem accusantium doloremque laudantium, totam rem aperiam, eaque ipsa quae ab illo inventore veritatis et quasi architecto beatae vitae dicta sunt explicabo sed ut perspiciatis unde omnis iste natus error sit voluptatem accusantium.</p>
  <div class="btn" style="left:161px;top:1593px;width:122px;height:37px">Read more</div>
  <div class="globe"><div class="globe__fill" role="img" aria-label="Sketched world globe"></div></div>

  <!-- Our Technology -->
  <section class="tech" role="img" aria-label="Dark network of connected device icons"></section>
  <h2 class="heading abs" style="left:0;top:1785px;width:1200px;text-align:center;font-size:32px;color:var(--white)">Our Technology</h2>
  <p class="tech__text">Lorem ipsum dolor sit amet, consectetuer adipiscing elit, sed diam nonummy nibh euismod tincidunt ut laoreet dolore magna aliquam erat volutpat. Ut wisi enim ad minim veniam, quis nostrud exerci tation ullamcorper suscipit lobortis nisl ut aliquip ex ea commodo consequat. Duis autem vel eum iriure dolor in hendrerit in vulputate velit esse molestie consequat, vel illum dolore eu feugiat nulla facilisis at vero eros.</p>
  <div class="btn btn--light" style="left:535px;top:1972px;width:130px;height:36px">Find out more</div>

  <!-- Feature cards -->
  <div class="card" style="left:5px;width:582px">
    <div role="img" aria-label="Colleagues reviewing work together at a laptop" style="position:absolute;inset:0;background:linear-gradient(120deg,#c7814e 0%,#9a6a4c 45%,#d8b79a 100%)"></div>
    <svg class="abs" style="left:250px;top:135px" width="94" height="94" viewBox="0 0 94 94" aria-hidden="true">
      <circle cx="47" cy="47" r="43" fill="rgba(255,255,255,.12)" stroke="#fff" stroke-width="4"/>
      <path d="M38 30 L64 47 L38 64 Z" fill="#fff"/>
    </svg>
    <div class="abs" style="left:0;top:294px;width:582px;height:99px;background:var(--overlay)"></div>
    <div class="card__date" style="left:35px;top:313px">01.08.2016</div>
    <div class="abs" style="left:35px;top:348px;color:var(--white);font-size:17px">YOU SEE EVERY PIECE OF WORK</div>
  </div>
  <div class="card" style="left:592px;width:297px">
    <div role="img" aria-label="Dimmed photo of a person using a tablet" style="position:absolute;inset:0;background:linear-gradient(180deg,#2a2c30 0%,#3c3f44 60%,#2e3034 100%)"></div>
    <div class="card__date" style="left:14px;top:25px">01.08.2016</div>
    <p class="card__text" style="left:14px;top:65px;width:272px">Within your timeline you'll see everything that we're working on, what tasks we have in line to do next and what we've delivered for your business.</p>
  </div>
  <div class="card" style="left:896px;width:299px">
    <div role="img" aria-label="Dimmed photo of a person working at a desk" style="position:absolute;inset:0;background:linear-gradient(180deg,#2b2d31 0%,#44474d 60%,#303236 100%)"></div>
    <div class="card__date" style="left:18px;top:25px">01.08.2016</div>
    <p class="card__text" style="left:18px;top:65px;width:270px">Plenix will become a part of your marketing team and that means visibility on all channels and other media. We'll ensure that campaign are integrated. cross channel</p>
  </div>

  <!-- Case studies -->
  <section class="cases"></section>
  <h2 class="heading abs" style="left:0;top:2518px;width:1200px;text-align:center;font-size:32px">Case Studies</h2>
  <p class="abs" style="left:230px;top:2572px;width:740px;text-align:center;font-size:10.5px;line-height:17px">Sed ut perspiciatis unde omnis iste natus error sit voluptatem accusantium doloremque laudantium, totam rem aperiam, eaque ipsa quae ab illo inventore veritatis et quasi architecto beatae vitae dicta sunt explicabo.</p>

  <div class="case__img" style="left:161px;background:linear-gradient(135deg,#3a2a22 0%,#c06a3a 55%,#e9d7c7 100%)" role="img" aria-label="Tablet on a desk with glowing connection icons"></div>
  <div class="case__title" style="left:161px">Technology</div>
  <p class="case__text" style="left:161px">Sed ut perspiciatis unde omnis iste natus error sit voluptatem accusantium doloremque laudantium, totam rem aperiam, eaque ipsa quae ab illo inventore veritatis et quasi architecto beatae vitae dicta sunt explicabo.</p>
  <div class="btn" style="left:161px;top:2971px;width:115px;height:37px">Read more</div>

  <div class="case__img" style="left:463px;background:linear-gradient(135deg,#1b3d7a 0%,#3f8fd8 50%,#b9d9f2 100%)" role="img" aria-label="Hand touching a bright blue digital screen"></div>
  <div class="case__title" style="left:463px">Finibus Bonorum</div>
  <p class="case__text" style="left:463px">Sed ut perspiciatis unde omnis iste natus error sit voluptatem accusantium doloremque laudantium, totam rem aperiam, eaque ipsa quae ab illo inventore veritatis et quasi architecto beatae vitae dicta sunt explicabo.</p>
  <div class="btn" style="left:463px;top:2971px;width:115px;height:37px">Read more</div>

  <div class="case__img" style="left:765px;background:linear-gradient(135deg,#2e3a34 0%,#6d7b74 50%,#c9c2b4 100%)" role="img" aria-label="Hands holding a smartphone outdoors"></div>
  <div class="case__title" style="left:765px">BonorumMalorum</div>
  <p class="case__text" style="left:765px">Sed ut perspiciatis unde omnis iste natus error sit voluptatem accusantium doloremque laudantium, totam rem aperiam, eaque ipsa quae ab illo inventore veritatis et quasi architecto beatae vitae dicta sunt explicabo.</p>
  <div class="btn" style="left:765px;top:2971px;width:115px;height:37px">Read more</div>

  <!-- Contact -->
  <section class="contact" role="img" aria-label="Dark faded city background"></section>
  <h2 class="heading abs" style="left:0;top:3128px;width:1200px;text-align:center;font-size:32px;color:var(--white)">Contact Us</h2>
  <p class="abs" style="left:230px;top:3182px;width:740px;text-align:center;font-size:10.5px;line-height:17px;color:#d6d6d6">Lorem ipsum dolor sit amet, consectetuer adipiscing elit, sed diam nonummy nibh euismod tincidunt ut laoreet dolore magna aliquam erat volutpat. Ut wisi enim ad minim veniam, quis nostrud exerci tation ullamcorper suscipit lobortis nisl.</p>

  <div class="field" style="left:150px;top:3263px;width:212px;height:37px">Name</div>
  <div class="field" style="left:150px;top:3300px;width:212px;height:38px">Email</div>
  <div class="field" style="left:150px;top:3338px;width:212px;height:37px">Phone Number</div>
  <div class="field" style="left:362px;top:3263px;width:305px;height:112px;align-items:flex-start;padding-top:12px">Message</div>
  <div class="submit">SUBMIT</div>

  <div class="info" style="left:713px">Lorem ipsum dolor sit amet, consectetur adipiscing elit.<br><br>E: info@plenix-example.com<br>P: 1800-555-0142</div>
  <div class="info" style="left:896px">Lorem ipsum dolor sit amet, consectetur adipiscing elit.<br><br>E: info@plenix-example.com<br>P: 1800-555-0142</div>
  <div class="social" aria-label="Social links"><i></i><i></i><i></i><i></i><i></i></div>

  <div class="footer-line"></div>
  <p class="copyright">Copyright © 2016. plenix-example.com. All Rights Reserved.</p>

</div>
</body>
</html>
```